The Rapport Compass - A coaching tool for high level sales people

I would like a design for a professional development tool called The Rapport Compass. I will use this tool in powerpoint presentations and with individual coaching clients to help them understand how to connect with people quickly. I would like the triangle to be the infinity triangle that I have attached and for the sides of the triangle to be called Emotional Intelligence, Social Intelligence and Practical Empathy. Inside the triangle should be the word trust. For colours and style, see our logo, attached and our website www.theharbourofpropertysales.example It should be professional but natural and a touch of whimsy may work well.

Target Market(s)

Real Estate Agents in Canada and the US who are open to professional development

Industry/Entity Type

Real Estate

Font styles to use
Sans Serif

Colors
32a6d6
85acd3
3176b5
0858a5
85cae6
85abd2
ec1f27

Requirements
Must have
• must have a great feel. We are called The Harbour of Property Sales because we find ways for salespeople to excel in sales using their natural strengths, having authentic conversations and understanding their clients and customers in a deep and meaningful way. The colours should align with our branding as per the website.
Nice to have
• It should come across as professional but not too formal. A subtle sense of nature would be a benefit/
Should not have
• Should not be bold and should not use colours not used in our branding

```html
<!DOCTYPE html>
<html lang="en">
<head>
<meta charset="utf-8">
<title>The Rapport Compass</title>
<link rel="stylesheet" href="https://fonts.googleapis.com/css2?family=Source+Sans+3:wght@400&display=swap">
<style>
  :root {
    --backdrop: #1c1c1c;
    --paper: #ffffff;
    --ink: #111111;
    --label-ink: #3a3a3a;
    --line-blue: #3176b5;
    --trust-red: #ec1f27;
  }
  html, body {
    margin: 0;
    padding: 0;
    width: 1200px;
    height: 1000px;
    overflow: hidden;
    background: var(--backdrop);
  }
  .canvas {
    width: 1200px;
    height: 1000px;
    display: block;
  }
  .backdrop { fill: var(--backdrop); }
  .sheet { fill: var(--paper); }
  .tool-title {
    font-family: "Source Sans 3", "Myriad Pro", sans-serif;
    font-weight: 400;
    font-size: 52px;
    fill: var(--ink);
  }
  .side-label {
    font-family: "Source Sans 3", "Myriad Pro", sans-serif;
    font-weight: 400;
    font-size: 42px;
    letter-spacing: 0.6px;
    fill: var(--label-ink);
  }
  .core-word {
    font-family: "Source Sans 3", "Myriad Pro", sans-serif;
    font-weight: 400;
    font-size: 58px;
    fill: var(--trust-red);
  }
  .triangle-stroke {
    fill: none;
    stroke: var(--line-blue);
    stroke-width: 8;
    stroke-linejoin: miter;
    stroke-linecap: butt;
  }
</style>
</head>
<body>
<svg class="canvas" viewBox="0 0 1200 1000" xmlns="http://www.w3.org/2000/svg">
  <rect class="backdrop" x="0" y="0" width="1200" height="1000"/>
  <rect class="sheet" x="175" y="62" width="838" height="826"/>

  <g class="compass">
    <text class="tool-title" x="592" y="196" text-anchor="middle">The Rapport Compass</text>

    <g class="infinity-triangle">
      <polyline class="triangle-stroke" points="587,232 314,703 793,701"/>
      <polyline class="triangle-stroke" points="302,729 851,726 601,305"/>
      <polyline class="triangle-stroke" points="361,678 600,252 878,718"/>
    </g>

    <text class="side-label side-left" text-anchor="middle"
          transform="translate(420 462) rotate(-60)">Emotional Intelligence</text>
    <text class="side-label side-right" text-anchor="middle"
          transform="translate(760 474) rotate(59)">Social Intelligence</text>
    <text class="side-label side-bottom" x="579" y="776" text-anchor="middle">Practical Empathy</text>

    <text class="core-word" x="582" y="556" text-anchor="middle">TRUST</text>
  </g>
</svg>
</body>
</html>
```